Velmarind

We need a website redesign for a Wordpress-based template. We have WP and Elementor and are looking for a template to modernise the existing website at http://www.velmarind.co.uk. we can handle the relocation of the content but want a new fresh look. As an example, http://brovy.io looks nice.

```html
<!DOCTYPE html>
<html lang="en">
<head>
<meta charset="utf-8">
<title>Velmarind – Home</title>
<link rel="stylesheet" href="https://fonts.googleapis.com/css2?family=Nunito+Sans:wght@300;400;600&family=Open+Sans:wght@600;700&display=swap">
<style>
:root{
  --green:#3a9a0b;
  --yellow:#ffff00;
  --ink:#2b2b2b;
  --text:#4a4a4a;
  --muted:#666;
  --band:#e9e9e9;
  --white:#fff;
  --hero-a:#0b2f5c;
  --hero-b:#1f77b4;
  --hero-c:#041529;
}
*{box-sizing:border-box;margin:0;padding:0}
html,body{width:814px;height:1200px;overflow:hidden;background:var(--white)}
body{position:relative;font-family:"Nunito Sans",sans-serif;color:var(--text)}
.abs{position:absolute}
.site-header{position:absolute;left:0;top:0;width:814px;height:64px;background:var(--white)}
.brand{position:absolute;left:76px;top:14px;display:flex;align-items:center;gap:8px;font-size:28px;font-weight:400;color:var(--ink);letter-spacing:.5px}
.brand-dot{width:18px;height:18px;border-radius:50%;background:var(--yellow);border:0}
.main-nav a{position:absolute;top:31px;font-size:12px;color:var(--muted);text-decoration:none}
.main-nav a.active{color:var(--green)}
.hero{position:absolute;left:0;top:64px;width:814px;height:376px;
  background:radial-gradient(ellipse at 45% 40%,var(--hero-b) 0%,var(--hero-a) 55%,var(--hero-c) 100%)}
.hero h1{position:absolute;left:0;width:814px;top:142px;text-align:center;font-family:"Open Sans",sans-serif;font-weight:700;font-size:29px;color:var(--white);text-shadow:0 1px 3px rgba(0,0,0,.3)}
.hero p{position:absolute;left:0;width:814px;top:180px;text-align:center;font-family:"Open Sans",sans-serif;font-weight:600;font-size:19px;color:var(--white);text-shadow:0 1px 3px rgba(0,0,0,.3)}
.hero-arrow{position:absolute;left:395px;top:228px}
.hero-dots{position:absolute;left:382px;top:347px;display:flex;gap:6px}
.hero-dots span{width:8px;height:8px;border-radius:50%;background:var(--white)}
.hero-dots span.current{background:transparent;border:1.5px solid var(--white)}
.mission h2{position:absolute;left:0;width:814px;top:476px;text-align:center;font-weight:400;font-size:24px;color:var(--ink)}
.mission p{position:absolute;left:120px;width:574px;text-align:center;font-size:10.5px;line-height:17px;color:var(--text)}
.card{position:absolute;top:646px;width:318px;height:191px;padding:0}
.card-services{left:84px;background:var(--yellow);color:var(--ink)}
.card-switching{left:411px;background:var(--green);color:var(--white)}
.card svg{position:absolute;left:24px;top:26px}
.card h3{position:absolute;left:29px;top:82px;font-weight:400;font-size:16px}
.card p{position:absolute;left:31px;top:107px;width:270px;font-size:10.5px;line-height:14px}
.card .btn{position:absolute;left:32px;top:147px;width:82px;height:24px;border:1.5px solid currentColor;font-size:9px;font-weight:600;line-height:21px;text-align:center;text-decoration:none;color:inherit}
.reviews{position:absolute;left:0;top:870px;width:814px;height:234px;background:var(--band)}
.reviews h2{position:absolute;left:0;width:814px;top:25px;text-align:center;font-weight:400;font-size:19px;color:var(--ink)}
.quote-box{position:absolute;left:196px;top:75px;width:422px;height:92px;background:var(--white);border:1px solid #ddd}
.quote-box p{position:absolute;left:14px;right:14px;top:32px;text-align:center;font-size:10.5px;line-height:17px;color:var(--text)}
.quote-tail{position:absolute;left:400px;top:166px;width:12px;height:12px;background:var(--white);transform:rotate(45deg);border-right:1px solid #ddd;border-bottom:1px solid #ddd}
.quote-mark{position:absolute;left:389px;top:65px}
.reviewer{position:absolute;left:0;width:814px;top:183px;text-align:center;font-size:10.5px;color:var(--ink)}
.rev-arrow{position:absolute;top:100px}
.site-footer .links a{position:absolute;top:1131px;font-size:11.5px;color:var(--muted);text-decoration:none}
.copyright{position:absolute;left:82px;top:1155px;font-size:10.5px;color:var(--muted)}
.social{position:absolute;top:1126px;width:24px;height:24px;border-radius:50%;background:var(--green)}
</style>
</head>
<body>
<header class="site-header">
  <div class="brand">Velmarind <span class="brand-dot"></span></div>
  <nav class="main-nav">
    <a class="active" href="#" style="left:323px">Home</a>
    <a href="#" style="left:378px">About</a>
    <a href="#" style="left:433px">Therapeutic Switching</a>
    <a href="#" style="left:570px">Services</a>
    <a href="#" style="left:636px">Blog</a>
    <a href="#" style="left:684px">Contact</a>
  </nav>
</header>

<section class="hero" role="img" aria-label="Close-up of a glowing blue DNA double helix">
  <h1>Based in Cambridge, England</h1>
  <p>Discovering &amp; developing secondary uses for existing drugs</p>
  <svg class="hero-arrow" width="24" height="14" viewBox="0 0 24 14"><polyline points="1,1 12,12 23,1" fill="none" stroke="#fff" stroke-width="2.5"/></svg>
  <div class="hero-dots"><span class="current"></span><span></span><span></span><span></span></div>
</section>

<section class="mission">
  <h2>Our Mission</h2>
  <p style="top:515px">Velmarind Ltd was established in 2008 to provide collaborative services to companies seeking expert advice in the area novel uses for existing drugs, or ‘drug repurposing’</p>
  <p style="top:549px">Velmarind' founder was an early advocate of drug repurposing and has a strong track record of achievement in the area. The rate-limiting step for the realisation of the strategy's full potential is often the adoption of developmental propositions and their commercialisation, rather than the innovation.</p>
</section>

<article class="card card-services">
  <svg width="60" height="46" viewBox="0 0 60 46" fill="none" stroke="#111" stroke-width="2">
    <path d="M30 44 L8 22 A11 11 0 0 1 30 8 A11 11 0 0 1 52 22 Z"/>
    <polyline points="1,22 18,22 23,14 30,32 36,18 40,22 58,22"/>
  </svg>
  <h3>Our Services</h3>
  <p>Praesent elementum elit at tellus nec ultricies sit amet porttitor mattis enim In massa libero interdum</p>
  <a class="btn" href="#">READ MORE</a>
</article>
<article class="card card-switching">
  <svg width="50" height="58" viewBox="0 0 50 58" fill="none" stroke="#fff" stroke-width="2">
    <path d="M40 2 C40 20 8 30 8 56"/>
    <path d="M48 8 C30 16 20 40 2 46"/>
    <line x1="34" y1="12" x2="42" y2="16"/><line x1="26" y1="20" x2="36" y2="26"/>
    <line x1="18" y1="30" x2="26" y2="36"/><line x1="12" y1="40" x2="18" y2="46"/>
  </svg>
  <h3>Therapeutic switching</h3>
  <p>Praesent elementum elit at tellus nec ultricies sit amet porttitor mattis enim In massa libero interdum</p>
  <a class="btn" href="#">READ MORE</a>
</article>

<section class="reviews">
  <h2>Latest Reviews</h2>
  <svg class="rev-arrow" style="left:150px" width="18" height="42" viewBox="0 0 18 42"><polyline points="16,1 2,21 16,41" fill="none" stroke="#aaa" stroke-width="1.2"/></svg>
  <svg class="rev-arrow" style="left:642px" width="18" height="42" viewBox="0 0 18 42"><polyline points="2,1 16,21 2,41" fill="none" stroke="#aaa" stroke-width="1.2"/></svg>
  <div class="quote-box">
    <p>'A fascinating read...lot more balanced and intellectually satisfying than the much higher profile Bitter Remedies...essential reading</p>
  </div>
  <div class="quote-tail"></div>
  <svg class="quote-mark" width="30" height="30" viewBox="0 0 30 30">
    <circle cx="15" cy="15" r="15" fill="var(--green)"/>
    <path d="M13 10 C9 11 8 15 10 19 M20 10 C16 11 15 15 17 19" fill="none" stroke="#fff" stroke-width="2.2" stroke-linecap="round"/>
  </svg>
  <div class="reviewer">Medicines Information Director, Northvale Health</div>
</section>

<footer class="site-footer">
  <nav class="links">
    <a href="#" style="left:82px">Home</a>
    <a href="#" style="left:136px">About</a>
    <a href="#" style="left:191px">Therapeutic Switching</a>
    <a href="#" style="left:329px">Services</a>
    <a href="#" style="left:395px">Blog</a>
    <a href="#" style="left:443px">Contact</a>
  </nav>
  <div class="copyright">© 2017 Company Name &nbsp;All right reserved &nbsp;Term of Use</div>
  <a class="social" href="#" aria-label="Social link 1" style="left:613px"></a>
  <a class="social" href="#" aria-label="Social link 2" style="left:645px"></a>
  <a class="social" href="#" aria-label="Social link 3" style="left:677px"></a>
  <a class="social" href="#" aria-label="Social link 4" style="left:709px"></a>
</footer>
</body>
</html>
```